Modern Homepage Design for brenvik.nl – Fish & Chicken Food Webshop

Brenvik.nl is an online store that sells fish and chicken food. The design should be visually appealing, easy to navigate, and optimized for e-commerce. We want a layout that helps customers quickly find what they need and encourages them to explore our products.
A good example of the style and structure we like is dierkamp.nl – clean layout, clear product focus, and user-friendly navigation.
Brand Colors (must be used):
Orange: #f7a441
Dark Gray: #3c3c3b
White: #ffffff
Please use these colors consistently throughout the design.
Homepage Requirements:
The homepage should include the following sections:
Main Slider / Hero Banner
A large, eye-catching slider at the top of the page to highlight promotions or featured categories.
Category Blocks
A section with clear, clickable blocks or tiles that link to main product categories (e.g., Fish Food, Chicken Food, Accessories).
Featured Products
A section showcasing selected or best-selling products.
Special Offers / Promotions
A space to highlight current deals or limited-time offers.
Three Banners in a Row
A section with three horizontal banners side by side, which can be used for promotions, shipping info, or other key messages.
Unique Selling Points (USPs)
A section that briefly explains what makes our store different (e.g., fast delivery, high-quality feed, trusted by professionals).
SEO Content Block
A short paragraph of text for SEO purposes (use Lorem Ipsum for dummy content).
Footer Design
Include space for contact information, navigation links, and social media.
Design Notes:
The design must be responsive and mobile-friendly.
Focus on clean layout, good spacing, and easy navigation.
Use modern fonts and a clear visual hierarchy.
We are only looking for the homepage design at this stage, but we may work with the selected designer on additional pages later.
Deliverables:
Homepage design in layered PSD, Figma, or Adobe XD format
Any fonts and assets used
Preview images/mockups
We look forward to seeing your ideas and working with a designer who can bring our brand to life with a fresh and functional homepage design.
Let us know if you have any questions.
Hobby Animal Keepers, Pet Owners
Animal Nutrition & Feed
2 page

```html
<!DOCTYPE html>
<html lang="en">
<head>
<meta charset="utf-8">
<title>Brenvik – Fish &amp; Chicken Food Webshop</title>
<link href="https://fonts.googleapis.com/css2?family=Raleway:wght@500;600;700&family=Poppins:wght@400;500;600&display=swap" rel="stylesheet">
<style>
:root{
  --orange:#f7a441;
  --orange-deep:#ef8a1f;
  --dark:#3c3c3b;
  --white:#ffffff;
  --cream:#fdf1e4;
  --cream-deep:#f9dcbd;
  --grey-tile:#f4f4f4;
  --line:#e6e6e6;
  --red:#e23b2e;
}
*{box-sizing:border-box;margin:0;padding:0}
html,body{width:1200px;height:4032px;overflow:hidden;background:var(--white)}
body{position:relative;font-family:'Poppins',sans-serif;color:var(--dark)}
.abs{position:absolute}
.head{font-family:'Raleway',sans-serif;font-weight:600;text-transform:uppercase;color:var(--dark)}
.hl{color:var(--orange)}
.btn{position:absolute;height:41px;border-radius:21px;background:var(--orange);color:var(--white);font-family:'Raleway',sans-serif;font-weight:600;font-size:13px;text-transform:uppercase;display:flex;align-items:center;justify-content:center;gap:10px}
.sec-title{position:absolute;left:0;width:1200px;text-align:center;font-size:27px;display:flex;justify-content:center;align-items:center;gap:12px}
.paw{width:24px;height:24px}

/* nav */
.nav{left:128px;top:39px;width:942px;height:72px;background:var(--white);border-radius:36px;box-shadow:0 4px 16px rgba(0,0,0,.06)}
.nav-links{left:58px;top:28px;display:flex;gap:26px;font-family:'Raleway',sans-serif;font-weight:600;font-size:12px}
.nav-links .on{color:var(--orange)}
.brand{font-family:'Raleway',sans-serif;font-weight:700;color:var(--dark);display:flex;align-items:center;gap:6px}
.brand .dot{width:26px;height:26px;border-radius:50%;background:var(--orange)}
.nav-icons{right:50px;top:21px;display:flex;gap:22px}
.nav-icons span{width:31px;height:31px;border:1px solid var(--line);border-radius:6px;display:flex;align-items:center;justify-content:center}

/* categories */
.cat{position:absolute;top:694px;width:172px;height:226px;border-radius:8px;text-align:center}
.cat .pic{position:absolute;left:34px;top:20px;width:104px;height:104px;border-radius:50%}
.cat b{position:absolute;top:150px;left:0;width:100%;font-family:'Raleway',sans-serif;font-weight:600;font-size:15px}
.cat i{position:absolute;top:183px;left:0;width:100%;font-style:normal;font-size:11px;color:#777}

.promo{position:absolute;top:1097px;width:314px;height:184px;border-radius:8px;overflow:hidden;color:var(--white);font-family:'Raleway',sans-serif;font-weight:700}
.promo .t1{position:absolute;left:20px;top:21px;font-size:12px;font-weight:600}
.promo .t2{position:absolute;left:20px;top:46px;font-size:14px;line-height:25px;width:160px}
.promo .t3{position:absolute;left:20px;top:129px;font-size:10px;font-weight:600}
.promo .t4{position:absolute;left:20px;top:150px;font-size:14px}
.promo .pack{position:absolute;right:26px;top:18px;width:88px;height:148px;border-radius:8px}

.usp-num{font-family:'Raleway',sans-serif;font-weight:600;font-size:24px;color:var(--orange)}
.usp-lbl{font-family:'Raleway',sans-serif;font-weight:600;font-size:15px;line-height:34px;text-transform:uppercase}

.card{position:absolute;width:219px;height:338px;border:2px solid #eee;border-radius:12px;overflow:hidden;text-align:center}
.card .img{position:absolute;left:0;top:0;width:100%;height:206px;background:var(--grey-tile)}
.card .img span{position:absolute;left:60px;top:24px;width:96px;height:160px;border-radius:10px}
.card .badge{position:absolute;right:10px;top:12px;background:var(--red);color:var(--white);font-size:9px;font-weight:600;padding:4px 8px;border-radius:3px}
.card .stars{position:absolute;top:228px;left:0;width:100%;color:var(--orange-deep);font-size:15px;letter-spacing:3px}
.card .name{position:absolute;top:264px;left:0;width:100%;font-family:'Raleway',sans-serif;font-weight:600;font-size:13px;color:var(--orange-deep);text-transform:uppercase}
.card .price{position:absolute;top:296px;left:0;width:100%;font-family:'Raleway',sans-serif;font-weight:600;font-size:17px}

.info{position:absolute;top:2738px;width:314px;height:210px;background:#fdf0e2;border-radius:8px;overflow:hidden;font-family:'Raleway',sans-serif;font-weight:600;text-transform:uppercase}
.info .k{position:absolute;left:24px;top:30px;font-size:12px}
.info .h{position:absolute;left:24px;top:64px;font-size:14px;line-height:29px;color:var(--orange-deep)}
.info .a{position:absolute;left:24px;font-size:13px;text-decoration:underline}
.info .art{position:absolute;border-radius:8px}

.about-p{font-size:15px;line-height:34px;color:#555}
.fcol{position:absolute;top:3727px}
.fcol h4{font-family:'Raleway',sans-serif;font-weight:600;font-size:16px;color:var(--orange);text-transform:uppercase;margin-bottom:22px}
.fcol li{list-style:none;font-family:'Raleway',sans-serif;font-weight:600;font-size:13px;text-transform:uppercase;height:36px}
.pay{display:flex;gap:14px;right:108px;top:3979px}
.pay span{width:26px;height:17px;border-radius:3px;background:#d9dde6}
</style>
</head>
<body>

<!-- hero -->
<svg class="abs" style="left:0;top:0" width="1200" height="560" aria-hidden="true">
  <path d="M0 0H1200V520C1080 540 980 505 860 520S600 545 480 525S220 505 0 530Z" fill="var(--cream)"/>
  <path d="M0 0H480C500 40 470 95 380 100S220 140 140 170S40 175 0 170Z" fill="var(--cream-deep)"/>
</svg>

<header class="abs nav">
  <nav class="abs nav-links"><span class="on">Home</span><span>About</span><span>Shop</span><span>Contact</span></nav>
  <div class="abs brand" style="left:395px;top:18px;font-size:34px"><span class="dot"></span>Brenvik</div>
  <div class="abs nav-icons">
    <span><svg width="14" height="14" viewBox="0 0 24 24" fill="none" stroke="#3c3c3b" stroke-width="2"><circle cx="12" cy="8" r="4"/><path d="M4 21c1-5 15-5 16 0"/></svg></span>
    <span><svg width="13" height="13" viewBox="0 0 24 24" fill="none" stroke="#3c3c3b" stroke-width="2.4"><circle cx="10" cy="10" r="7"/><path d="M15 15l6 6"/></svg></span>
    <span><svg width="14" height="14" viewBox="0 0 24 24" fill="none" stroke="#3c3c3b" stroke-width="2"><path d="M5 8h14l-1 13H6z"/><path d="M9 8V6a3 3 0 016 0v2"/></svg></span>
  </div>
</header>

<div class="abs head" style="left:109px;top:184px;font-size:18px;font-weight:500;display:flex;align-items:center;gap:12px">Brenvik <span style="width:30px;height:2px;background:var(--orange)"></span></div>
<h1 class="abs head" style="left:109px;top:228px;font-size:36px">A <span class="hl">Pet Lovers</span> Pardise</h1>
<p class="abs" style="left:109px;top:296px;width:480px;font-size:16px;line-height:39px">Up to 25% off on selected feed and accessories. Top-quality feed for strong and productive chickens</p>
<a class="btn" style="left:109px;top:402px;width:147px">Shop Now <span>&rarr;</span></a>
<div class="abs" role="img" aria-label="Curly brown dog holding a food bowl, surrounded by hand-lettered words vegetables, fruit, meat, fish and cereals" style="left:620px;top:150px;width:470px;height:330px;border-radius:50%;background:radial-gradient(circle at 55% 55%,#f6c79a 0 45%,rgba(253,241,228,0) 46%)"></div>

<!-- categories -->
<h2 class="sec-title head" style="top:610px"><svg class="paw" viewBox="0 0 24 24" fill="var(--orange)"><ellipse cx="12" cy="16" rx="5" ry="4"/><circle cx="5" cy="10" r="2.3"/><circle cx="9" cy="5.5" r="2.3"/><circle cx="15" cy="5.5" r="2.3"/><circle cx="19" cy="10" r="2.3"/></svg><span>Browse by <span class="hl">Categories</span></span></h2>

<a class="cat" style="left:111px;background:#c8e4b0"><span class="pic" role="img" aria-label="Leaping trout" style="background:radial-gradient(#8aa08a,#3f5a4a)"></span><b>Fish Food</b><i>15 items</i></a>
<a class="cat" style="left:312px;background:#f9c0b6"><span class="pic" role="img" aria-label="Brown hen with eggs" style="background:radial-gradient(#c7743c,#6d3a1c)"></span><b>Chicken Food</b><i>15 items</i></a>
<a class="cat" style="left:514px;background:#a8e6f3"><span class="pic" role="img" aria-label="Pet toys and accessories" style="background:radial-gradient(#2f8fd0,#e24a4a)"></span><b>Accessories</b><i>15 items</i></a>
<a class="cat" style="left:714px;background:#f8dc8a"><span class="pic" role="img" aria-label="Golden retriever" style="background:radial-gradient(#e7b26b,#b27a38)"></span><b>Dog Food</b><i>15 items</i></a>
<a class="cat" style="left:916px;background:#f4c6f2"><span class="pic" role="img" aria-label="Robin on a branch" style="background:radial-gradient(#c9763b,#5d5548)"></span><b>Birds Food</b><i>15 items</i></a>

<a class="btn" style="left:488px;top:970px;width:223px">View All Products <span>&rarr;</span></a>

<!-- promos -->
<div class="promo" style="left:111px;background:#3e5a22">
  <svg class="abs" style="left:0;top:0" width="314" height="184"><path d="M170 184C200 120 260 100 314 90V184Z" fill="#7eaa3a"/></svg>
  <div class="t1">FIVE DAY SALE!</div><div class="t2">100% ORGANIC PET FOOD</div><div class="t3">SALE UP TO</div><div class="t4">50% OFF</div>
  <span class="pack" role="img" aria-label="Organic pet food bag" style="background:linear-gradient(#e7b24a,#7fb1d8)"></span>
</div>
<div class="promo" style="left:442px;background:#8b1010">
  <svg class="abs" style="left:0;top:0" width="314" height="184"><path d="M140 184C180 140 260 130 314 140V184Z" fill="#6e0c0c"/></svg>
  <div class="t1" style="top:20px;line-height:25px;font-size:14px;font-weight:700">PET FOOD &amp;<br>ACCESSORIES</div><div class="t3">SALE UP TO</div><div class="t4">40% OFF</div>
  <span class="abs" role="img" aria-label="Steel bowl full of kibble" style="left:140px;top:60px;width:160px;height:90px;border-radius:50%;background:radial-gradient(#b6652c,#777 70%)"></span>
</div>
<div class="promo" style="left:773px;background:#0c4453">
  <svg class="abs" style="left:0;top:0" width="314" height="184"><path d="M110 184C150 130 250 110 314 120V184Z" fill="#1f9a9c"/></svg>
  <div class="t1">FLASH SALE!</div><div class="t2">AFFORDABLE PET JOY AWAITS</div><div class="t3">SALE UP TO</div><div class="t4">35% OFF</div>
  <span class="pack" role="img" aria-label="Dog food bag" style="background:linear-gradient(#6a78c7,#2e3a8a)"></span>
</div>

<!-- USPs -->
<svg class="abs" style="left:0;top:1365px" width="1200" height="335" aria-hidden="true">
  <path d="M0 15C120 0 220 25 360 12S640 0 800 15S1080 25 1200 8V318C1080 330 960 305 800 320S520 335 380 318S140 305 0 325Z" fill="var(--cream)"/>
</svg>
<h2 class="sec-title head" style="top:1438px"><svg class="paw" viewBox="0 0 24 24" fill="var(--orange)"><ellipse cx="12" cy="16" rx="5" ry="4"/><circle cx="5" cy="10" r="2.3"/><circle cx="9" cy="5.5" r="2.3"/><circle cx="15" cy="5.5" r="2.3"/><circle cx="19" cy="10" r="2.3"/></svg><span>What makes our store <span class="hl">different</span></span></h2>

<div class="abs" style="left:108px;top:1525px;width:85px;height:85px;border-radius:50%;background:#ea7a25;display:flex;align-items:center;justify-content:center"><svg width="44" height="44" viewBox="0 0 24 24" fill="none" stroke="#fff" stroke-width="1.4"><path d="M2 7h12v9H2zM14 10h4l3 3v3h-7"/><circle cx="6" cy="17.5" r="1.8"/><circle cx="17" cy="17.5" r="1.8"/></svg></div>
<div class="abs" style="left:217px;top:1530px"><div class="usp-num">01</div><div class="usp-lbl">Fast Delivery</div></div>

<div class="abs" style="left:453px;top:1525px;width:85px;height:85px;border-radius:50%;background:#7cbb3c;display:flex;align-items:center;justify-content:center"><svg width="42" height="42" viewBox="0 0 24 24" fill="none" stroke="#fff" stroke-width="1.4"><path d="M12 3v10M8 6l4 4 4-4M4 15c4 0 6 2 8 5 2-3 4-5 8-5"/></svg></div>
<div class="abs" style="left:571px;top:1530px"><div class="usp-num">02</div><div class="usp-lbl">High-Quality Feed</div></div>

<div class="abs" style="left:842px;top:1525px;width:85px;height:85px;border-radius:50%;background:#ea4a8c;display:flex;align-items:center;justify-content:center"><svg width="42" height="42" viewBox="0 0 24 24" fill="none" stroke="#fff" stroke-width="1.4"><circle cx="12" cy="8" r="4"/><path d="M4 21c1-5 15-5 16 0M15 15l2 2 3-3"/></svg></div>
<div class="abs" style="left:953px;top:1530px"><div class="usp-num">03</div><div class="usp-lbl">Trusted by<br>Professionals</div></div>

<!-- products -->
<h2 class="sec-title head" style="top:1774px"><svg class="paw" viewBox="0 0 24 24" fill="var(--orange)"><ellipse cx="12" cy="16" rx="5" ry="4"/><circle cx="5" cy="10" r="2.3"/><circle cx="9" cy="5.5" r="2.3"/><circle cx="15" cy="5.5" r="2.3"/><circle cx="19" cy="10" r="2.3"/></svg><span>Our <span class="hl">Products</span></span></h2>

<div class="card" style="left:111px;top:1853px"><div class="img"><span role="img" aria-label="Shrimp food pellets bag" style="background:linear-gradient(#3a9bd0,#e46a2c)"></span></div><em class="badge">-10%</em><div class="stars">★★★★★</div><div class="name">Shrimp Food Pellets</div><div class="price">€6.99</div></div>
<div class="card" style="left:363px;top:1853px"><div class="img"><span role="img" aria-label="Scratch grains sack" style="background:linear-gradient(#a88a66,#c9a25a)"></span></div><em class="badge">POPULAR</em><div class="stars">★★★★★</div><div class="name">Scratch Grains</div><div class="price">€7.99</div></div>
<div class="card" style="left:616px;top:1853px"><div class="img"><span role="img" aria-label="Fish net with red handle" style="left:20px;top:60px;width:180px;height:80px;background:linear-gradient(110deg,#d62828 0 35%,#d9dde2 36%)"></span></div><em class="badge">BEST SELLER</em><div class="stars">★★★★★</div><div class="name">Fish Nets</div><div class="price">€5.50</div></div>
<div class="card" style="left:867px;top:1853px"><div class="img"><span role="img" aria-label="Aquarium test kit bottles with plants" style="left:20px;top:60px;width:180px;height:90px;background:linear-gradient(90deg,#4a8a3a,#6a6ad0,#c94a8a,#4a8a3a)"></span></div><em class="badge">-34%</em><div class="stars">★★★★★</div><div class="name">Aquarium Test Kits</div><div class="price">€9.99</div></div>

<div class="card" style="left:111px;top:2230px"><div class="img"><span role="img" aria-label="Premium fish food bag" style="background:linear-gradient(#2350a8,#e88a2c)"></span></div><em class="badge">-50%</em><div class="stars">★★★★★</div><div class="name">Tropical Fish Flakes</div><div class="price">€9.99</div></div>
<div class="card" style="left:363px;top:2230px"><div class="img"><span role="img" aria-label="Goldfish food sack" style="background:linear-gradient(#f0b04a,#e07a2a)"></span></div><em class="badge">POPULAR</em><div class="stars">★★★★★</div><div class="name">Goldfish Pellets</div><div class="price">€12.50</div></div>
<div class="card" style="left:616px;top:2230px"><div class="img"><span role="img" aria-label="Layer feed bag with hen" style="background:linear-gradient(#d8b060,#b8443a)"></span></div><em class="badge">BEST SELLER</em><div class="stars">★★★★★</div><div class="name">Chicken Layer Feed</div><div class="price">€18.90</div></div>
<div class="card" style="left:867px;top:2230px"><div class="img"><span role="img" aria-label="Starter feed bag with chick" style="background:linear-gradient(#e8c040,#5a6a2a)"></span></div><em class="badge">-30%</em><div class="stars">★★★★★</div><div class="name">Chicken Starter Feed</div><div class="price">€11.20</div></div>

<a class="btn" style="left:488px;top:2611px;width:223px">View All Products <span>&rarr;</span></a>

<!-- info banners -->
<div class="info" style="left:111px"><div class="k">Fast &amp; Reliable Delivery</div><div class="h">Delivered Fresh,<br>Right to your door</div><div class="a" style="top:140px">Shop Now</div><span class="art" role="img" aria-label="Spilled kibble with food tin and bowl" style="left:118px;top:100px;width:180px;height:95px;background:radial-gradient(#a86b3a,#fdf0e2 70%)"></span></div>
<div class="info" style="left:442px"><div class="k">Premium Quality Feed</div><div class="h">Trusted by farmers &amp;<br>enthusiasts</div><div class="a" style="top:140px">Explore Products</div><span class="art" role="img" aria-label="Beagle eating from a bowl" style="left:210px;top:40px;width:95px;height:165px;background:radial-gradient(#8a5a32,#fdf0e2 70%)"></span></div>
<div class="info" style="left:773px"><div class="k">Excellent Customer Service</div><div class="h">We're here to help</div><div class="a" style="top:104px">Contact Us</div><span class="art" role="img" aria-label="Group of dogs and cats" style="left:140px;top:95px;width:174px;height:115px;background:radial-gradient(#9a8a78,#fdf0e2 72%)"></span></div>

<!-- about -->
<svg class="abs" style="left:0;top:3030px" width="1200" height="490" aria-hidden="true">
  <path d="M598 12C760 0 900 20 1050 8S1160 5 1200 10V490H598Z" fill="var(--cream)"/>
</svg>
<div class="abs" role="img" aria-label="Woman kneeling beside a curly brown dog, pouring food into a bowl" style="left:0;top:3039px;width:598px;height:466px;background:linear-gradient(135deg,#ece9e3,#b58a62 60%,#7a4a2c);clip-path:polygon(0 2%,30% 0,60% 3%,100% 0,100% 100%,60% 97%,30% 100%,0 98%)"></div>
<h2 class="abs head" style="left:650px;top:3083px;font-size:27px;display:flex;align-items:center;gap:10px"><svg class="paw" viewBox="0 0 24 24" fill="var(--orange)"><ellipse cx="12" cy="16" rx="5" ry="4"/><circle cx="5" cy="10" r="2.3"/><circle cx="9" cy="5.5" r="2.3"/><circle cx="15" cy="5.5" r="2.3"/><circle cx="19" cy="10" r="2.3"/></svg><span>About <span class="hl">Brenvik</span></span></h2>
<p class="abs about-p" style="left:650px;top:3138px;width:440px">At Brenvik, we're passionate about providing the best nutrition for your animals. For years, we've been a trusted name among hobbyists, farmers, and professionals who value premium ingredients and consistent results.</p>
<p class="abs about-p" style="left:650px;top:3290px;width:440px">Our curated range of fish food, chicken feed, and accessories ensures every product meets the highest standards for freshness, safety, and performance.</p>
<a class="btn" style="left:650px;top:3422px;width:164px">Learn More <span>&rarr;</span></a>

<!-- footer -->
<div class="abs brand" style="left:109px;top:3588px;font-size:56px"><span class="dot" style="width:46px;height:46px"></span>Brenvik</div>
<div class="abs" style="left:664px;top:3597px;width:423px;height:44px;border:1px solid var(--line);border-radius:22px;display:flex;align-items:center;justify-content:space-between;padding:0 3px 0 26px">
  <span style="font-family:'Raleway',sans-serif;font-weight:600;font-size:12px;color:#666">EMAIL ADDRESS</span>
  <span style="background:var(--orange);color:#fff;height:36px;border-radius:18px;padding:0 20px;display:flex;align-items:center;font-size:11px;font-weight:500">SUBSCRIBE NOW</span>
</div>
<div class="abs" style="left:104px;top:3683px;width:990px;height:1px;background:var(--line)"></div>

<div class="fcol" style="left:109px"><h4>Customer Service</h4><ul><li>Contact</li><li>Shipping and Payment</li><li>Privacy</li><li>General</li><li>Sitemap</li></ul></div>
<div class="fcol" style="left:450px"><h4>My Account</h4><ul><li>My Account</li><li>Order History</li><li>Newsletter</li><li>Return</li></ul></div>
<div class="fcol" style="left:731px"><h4>Categories</h4><ul><li>Fish Food</li><li>Chicken Food</li><li>Accessories</li><li>Special Offers</li></ul></div>
<div class="fcol" style="left:1011px"><h4>Blog</h4><ul><li>Fish Food</li><li>Remaining</li></ul></div>

<div class="abs" style="left:104px;top:3953px;width:990px;height:1px;background:var(--line)"></div>
<div class="abs" style="left:111px;top:3982px;font-family:'Raleway',sans-serif;font-weight:600;font-size:13px">COPYRIGHT © 2025, BRENVIK. ALL RIGHTS RESERVED</div>
<div class="abs pay" aria-label="Accepted payment methods"><span></span><span></span><span></span><span></span><span></span><span></span></div>

</body>
</html>
```